Harbor Finwave Club Post Card

Looking for an original Eye Catching Post Card. This is for a Swim Club. We offer Swim Programs for age 4+

Highest Quality Coached Program

Small Team Provincial Champions

I want it to help fill my swim programs I offer Fitness Programs, Competitive and Swim Academy. Development swimmers to High Performance athletes.
I will attach a previous one i had done, but I want a really Eye Catching one - Double sided with information on one side as well. Or contact information.

"Harbor Finwave Club is a Coach Run Swim Club, bringing Passion & Uniqueness to our Athlete Centered Programs"

Target Market(s)

New Families to the Sport of Swimming

Industry/Entity Type

Club

Colors
3176b5
0355a3

Requirements
Must have
• Logo and My Own kids in the pictures not fab ones
Nice to have
• "Harbor Finwave Club is a Coach Run Swim Club, bringing Passion & Uniqueness to our Athlete Centered Programs"
Should not have
• Should not look like my original one at all

```html
<!DOCTYPE html>
<html lang="en">
<head>
<meta charset="utf-8">
<title>Harbor Finwave Club Post Card</title>
<link href="https://fonts.googleapis.com/css2?family=Anton&family=Open+Sans:ital,wght@0,400;0,600;0,700;1,600&display=swap" rel="stylesheet">
<style>
  :root {
    --club-blue: #3176b5;
    --deep-blue: #0355a3;
    --night-blue: #02346a;
    --sky: #d9eef8;
    --paper: #f3f9fc;
    --ink: #10233a;
    --white: #ffffff;
    --splash: #5cc3df;
  }
  * { margin: 0; padding: 0; box-sizing: border-box; }
  html, body { width: 746px; height: 1200px; overflow: hidden; background: var(--white); }
  body { font-family: "Open Sans", Arial, sans-serif; color: var(--ink); }
  .postcard { position: relative; width: 746px; height: 1200px; overflow: hidden; }

  /* ---------- Front side ---------- */
  .side-front {
    position: absolute; left: 0; top: 0; width: 746px; height: 597px; overflow: hidden;
    background: linear-gradient(150deg, var(--deep-blue) 0%, var(--club-blue) 55%, var(--night-blue) 100%);
  }
  .front-waves { position: absolute; inset: 0; width: 746px; height: 597px; }
  .front-header {
    position: absolute; left: 0; top: 0; width: 746px; height: 86px;
    display: flex; align-items: center; justify-content: space-between;
    padding: 0 30px; background: var(--night-blue);
  }
  .club-identity { display: flex; align-items: center; gap: 12px; }
  .club-identity .dot { width: 34px; height: 34px; border-radius: 50%; background: var(--splash); }
  .club-identity .club-name {
    font-family: "Anton", Impact, sans-serif; font-size: 30px; line-height: 1;
    letter-spacing: 1.5px; color: var(--white); text-transform: uppercase;
  }
  .header-tag { font-size: 15px; font-weight: 600; color: var(--sky); letter-spacing: 1px; text-transform: uppercase; }

  .hero-photo {
    position: absolute; left: 30px; top: 112px; width: 400px; height: 300px;
    border-radius: 18px; border: 5px solid var(--white);
    background: radial-gradient(circle at 50% 45%, #a6d6ec, #4a98cf 65%, #2a6eac);
  }
  .hero-copy { position: absolute; left: 460px; top: 108px; width: 262px; }
  .hero-title {
    font-family: "Anton", Impact, sans-serif; font-size: 50px; line-height: 56px;
    color: var(--white); text-transform: uppercase; letter-spacing: 1px;
  }
  .hero-title .accent { color: var(--splash); }
  .hero-sub { margin-top: 16px; font-size: 17px; line-height: 24px; font-weight: 700; color: var(--sky); }

  .champion-band {
    position: absolute; left: 0; top: 438px; width: 746px; height: 84px;
    display: flex; align-items: center; gap: 18px; padding-left: 30px;
    background: var(--white);
  }
  .champion-band .badge { width: 54px; height: 54px; border-radius: 50%; background: var(--deep-blue); flex: none; }
  .champion-band .champion-text {
    font-family: "Anton", Impact, sans-serif; font-size: 32px; line-height: 1;
    letter-spacing: 1px; color: var(--deep-blue); text-transform: uppercase;
  }
  .front-footer {
    position: absolute; left: 0; top: 522px; width: 746px; height: 75px;
    display: flex; align-items: center; justify-content: center;
    font-size: 18px; font-weight: 600; color: var(--white); letter-spacing: 0.5px;
  }

  .fold { position: absolute; left: 0; top: 597px; width: 746px; height: 6px; background: var(--white); }

  /* ---------- Back side ---------- */
  .side-back {
    position: absolute; left: 0; top: 603px; width: 746px; height: 597px; overflow: hidden;
    background: var(--paper);
  }
  .back-accent { position: absolute; left: 0; top: 0; width: 746px; height: 597px; }
  .mission-quote {
    position: absolute; left: 36px; top: 34px; width: 420px;
    font-size: 21px; line-height: 31px; font-weight: 600; font-style: italic;
    color: var(--club-blue);
  }
  .mission-quote .emphasis { color: var(--ink); }

  .contact-card {
    position: absolute; left: 484px; top: 30px; width: 232px; height: 170px;
    border-radius: 16px; background: var(--deep-blue); color: var(--white);
    padding: 20px 14px; text-align: center;
  }
  .contact-card .card-name {
    font-family: "Anton", Impact, sans-serif; font-size: 21px; letter-spacing: 1px;
    text-transform: uppercase; margin-bottom: 12px;
  }
  .contact-line {
    display: flex; align-items: center; justify-content: center; gap: 6px;
    font-size: 13px; line-height: 26px;
  }
  .contact-line svg { flex: none; }

  .programs { position: absolute; left: 36px; top: 228px; width: 420px; }
  .programs-title {
    font-family: "Anton", Impact, sans-serif; font-size: 28px; letter-spacing: 1px;
    color: var(--deep-blue); text-transform: uppercase; margin-bottom: 12px;
  }
  .program-list { list-style: none; }
  .program-list li {
    display: flex; align-items: flex-start; gap: 10px;
    font-size: 17px; line-height: 24px; margin-bottom: 12px; color: var(--ink);
  }
  .program-list svg { flex: none; margin-top: 3px; }

  .back-photo {
    position: absolute; left: 484px; top: 228px; width: 232px; height: 250px;
    border-radius: 16px; border: 4px solid var(--white);
    background: linear-gradient(180deg, #b9b3ad 0%, #7f7f86 60%, #3a4a7a 100%);
  }
  .back-footer {
    position: absolute; left: 0; top: 512px; width: 746px; height: 85px;
    display: flex; align-items: center; justify-content: center;
    background: var(--club-blue); color: var(--white);
    font-size: 19px; font-weight: 700; letter-spacing: 0.5px;
  }
</style>
</head>
<body>
<main class="postcard">

  <section class="side-front" aria-label="Front of post card">
    <svg class="front-waves" viewBox="0 0 746 597" aria-hidden="true">
      <path d="M0 540 C180 500 360 590 746 520 L746 597 L0 597 Z" fill="var(--night-blue)" opacity="0.7"/>
      <path d="M420 430 C540 380 640 400 746 360" stroke="var(--splash)" stroke-width="6" fill="none" opacity="0.6"/>
    </svg>

    <header class="front-header">
      <div class="club-identity">
        <span class="dot"></span>
        <span class="club-name">Harbor Finwave Club</span>
      </div>
      <span class="header-tag">Ages 4+</span>
    </header>

    <div class="hero-photo" role="img" aria-label="Club swimmer in a cap doing breaststroke in the pool"></div>

    <div class="hero-copy">
      <h1 class="hero-title">Swim<br>Programs<br><span class="accent">For Ages 4+</span></h1>
      <p class="hero-sub">Highest Quality<br>Coached Program</p>
    </div>

    <div class="champion-band">
      <span class="badge"></span>
      <span class="champion-text">Small Team Provincial Champions</span>
    </div>

    <p class="front-footer">Development swimmers to high performance athletes</p>
  </section>

  <div class="fold"></div>

  <section class="side-back" aria-label="Back of post card">
    <svg class="back-accent" viewBox="0 0 746 597" aria-hidden="true">
      <path d="M0 0 L746 0 L746 8 L0 8 Z" fill="var(--splash)"/>
    </svg>

    <p class="mission-quote">"Harbor Finwave Club is a Coach Run Swim Club, bringing <span class="emphasis">Passion &amp; Uniqueness</span> to our Athlete Centered Programs"</p>

    <address class="contact-card">
      <div class="card-name">Harbor Finwave Club</div>
      <div class="contact-line">
        <svg width="16" height="12" viewBox="0 0 16 12" aria-hidden="true"><rect x="0.7" y="0.7" width="14.6" height="10.6" fill="none" stroke="#fff" stroke-width="1.4"/><path d="M0.7 0.7 L8 7 L15.3 0.7" fill="none" stroke="#fff" stroke-width="1.4"/></svg>
        coachmara@harborfinwave.com
      </div>
      <div class="contact-line">www.harborfinwave.com</div>
      <div class="contact-line">
        <svg width="12" height="14" viewBox="0 0 12 14" aria-hidden="true"><rect x="1" y="0.7" width="10" height="12.6" rx="2" fill="none" stroke="#fff" stroke-width="1.4"/><circle cx="6" cy="10.5" r="1" fill="#fff"/></svg>
        555-014-2290
      </div>
    </address>

    <section class="programs">
      <h2 class="programs-title">Programs We Offer</h2>
      <ul class="program-list">
        <li><svg width="18" height="18" viewBox="0 0 18 18" aria-hidden="true"><circle cx="9" cy="9" r="9" fill="var(--club-blue)"/><path d="M5 9.5 L8 12 L13 6" stroke="#fff" stroke-width="2" fill="none"/></svg>Competitive Swimming</li>
        <li><svg width="18" height="18" viewBox="0 0 18 18" aria-hidden="true"><circle cx="9" cy="9" r="9" fill="var(--club-blue)"/><path d="M5 9.5 L8 12 L13 6" stroke="#fff" stroke-width="2" fill="none"/></svg>Swim Academy</li>
        <li><svg width="18" height="18" viewBox="0 0 18 18" aria-hidden="true"><circle cx="9" cy="9" r="9" fill="var(--club-blue)"/><path d="M5 9.5 L8 12 L13 6" stroke="#fff" stroke-width="2" fill="none"/></svg>Fitness Swim</li>
        <li><svg width="18" height="18" viewBox="0 0 18 18" aria-hidden="true"><circle cx="9" cy="9" r="9" fill="var(--club-blue)"/><path d="M5 9.5 L8 12 L13 6" stroke="#fff" stroke-width="2" fill="none"/></svg>Adult Swim &amp; Personal Training (online)</li>
        <li><svg width="18" height="18" viewBox="0 0 18 18" aria-hidden="true"><circle cx="9" cy="9" r="9" fill="var(--club-blue)"/><path d="M5 9.5 L8 12 L13 6" stroke="#fff" stroke-width="2" fill="none"/></svg>Coaching from developmental to high performance athletes</li>
      </ul>
    </section>

    <div class="back-photo" role="img" aria-label="Four club swimmers in caps and goggles posing together at a meet"></div>

    <p class="back-footer">New families welcome &middot; Swim programs for ages 4+</p>
  </section>

</main>
</body>
</html>
```